Sole practitioner CPA needs stationery design work

I need design art work for stationery which I can take to my printer. I require letterhead, business card, with comp's slip ,envelope. I would also like a word template in the letterhead format, as well as an email signature.
There are some professional requirements regarding the Tallywise Institute motif, and the words "Liability limited by a scheme approved under Professional Standards legislation". I have attached a mock up letterhead which shows these items

Target Market(s)

Small business owners who will expect to see a professional image

Industry/Entity Type

Business

Requirements
Must have
• Must have TWI logo and the words "Liability limited by a scheme approved under Professional Standards Legislation".
Nice to have
• I have attached a 'sample" that has the logo and the words. But the sample scheme is not important.

```html
<!DOCTYPE html>
<html lang="en">
<head>
<meta charset="utf-8">
<title>Harlow Accounting – Letterhead</title>
<link rel="stylesheet" href="https://fonts.googleapis.com/css2?family=Nunito:wght@700;800&family=Montserrat:wght@500;600;700&display=swap">
<style>
  :root {
    --navy: #1b3f6e;
    --blue-rule: #2a5d96;
    --orange: #e8731e;
    --paper: #ffffff;
    --ink: #1d2f4a;
  }
  * { box-sizing: border-box; margin: 0; padding: 0; }
  html, body { width: 849px; height: 1200px; overflow: hidden; background: var(--paper); }
  .letterhead { position: relative; width: 849px; height: 1200px; background: var(--paper); }

  .brand { position: absolute; left: 22px; top: 22px; display: flex; align-items: center; gap: 20px; }
  .brand-mark { width: 66px; height: 66px; border-radius: 50%; background: var(--orange); }
  .brand-name { font-family: "Nunito", sans-serif; font-weight: 800; font-size: 40px; line-height: 1; color: var(--navy); }
  .brand-tagline { font-family: "Montserrat", sans-serif; font-weight: 600; font-size: 16px; letter-spacing: 0.3px; color: var(--orange); margin-top: 10px; }

  .header-rule { position: absolute; left: 22px; right: 22px; top: 120px; height: 4px; background: var(--blue-rule); }

  .liability { position: absolute; left: 30px; top: 1036px; font-family: "Montserrat", sans-serif; font-weight: 600; font-size: 15.5px; color: var(--ink); text-transform: uppercase; letter-spacing: 0.1px; }
  .footer-rule { position: absolute; left: 22px; right: 22px; top: 1062px; height: 3px; background: var(--blue-rule); }

  .membership { position: absolute; left: 34px; top: 1078px; display: flex; align-items: center; gap: 18px; }
  .member-square { width: 86px; height: 86px; background: var(--navy); }
  .member-name { font-family: "Montserrat", sans-serif; font-weight: 700; font-size: 34px; color: var(--navy); }
  .member-statement { font-family: "Montserrat", sans-serif; font-weight: 500; font-size: 14px; line-height: 1.4; color: var(--navy); text-transform: uppercase; margin-left: 10px; }

  .footer-divider { position: absolute; left: 543px; top: 1074px; width: 3px; height: 96px; background: var(--navy); }
  .contact { position: absolute; left: 562px; top: 1078px; font-family: "Montserrat", sans-serif; font-size: 11.5px; line-height: 17px; color: var(--navy); text-transform: uppercase; }
  .contact strong { font-weight: 700; }
  .contact .abn { margin-top: 16px; }
</style>
</head>
<body>
  <main class="letterhead">
    <header class="brand">
      <div class="brand-mark"></div>
      <div>
        <div class="brand-name">Harlow Accounting</div>
        <div class="brand-tagline">CERTIFIED PRACTICING ACCOUNTANT</div>
      </div>
    </header>
    <div class="header-rule"></div>

    <p class="liability">Liability limited by a scheme approved under Professional Standards Legislation</p>
    <div class="footer-rule"></div>

    <footer>
      <div class="membership">
        <div class="member-square"></div>
        <span class="member-name">TWI</span>
        <p class="member-statement">Harlow Accounting<br>is a TWI practice</p>
      </div>
      <div class="footer-divider"></div>
      <address class="contact" style="font-style: normal;">
        <div><strong>PO Box 418 Marrowfield WA 6391</strong></div>
        <div><strong>Phone:</strong> 0400 555 218</div>
        <div>office@harlowaccounting.example</div>
        <div class="abn"><strong>ABN</strong> 12 345 678 901</div>
      </address>
    </footer>
  </main>
</body>
</html>
```